Cover for CD-single

MAVE is a young singer-songwriter and needs a CD cover design for her first single "Paper boats at dawn". Her song is about her best friend who recently moved from Europe to Australia with her family. But even though they now live on the other side of the world, they will always be there for each other.
You can use the picture attached or you can see it as an inspiration.
Please put the name of the artist: MAVE
and the name of the song on the cover: Paper boats at dawn

```html
<!DOCTYPE html>
<html lang="en">
<head>
<meta charset="utf-8">
<title>MAVE – Paper boats at dawn – CD single cover set</title>
<link rel="stylesheet" href="https://fonts.googleapis.com/css2?family=Marcellus&family=Lora&family=Arimo&display=swap">
<style>
  :root {
    --board: #5a5a5a;
    --paper: #ffffff;
    --spine: #2b2b2b;
    --artist-red: #d2202c;
    --ink: #1e1e1e;
    --label: #b4b4b4;
    --sky: #f4f7f9;
    --mountain-blue: #a9d3e6;
    --town-grey: #c9ccc8;
    --bench-red: #d8302e;
    --snow: #eceeea;
  }
  * { margin: 0; padding: 0; box-sizing: border-box; }
  html, body { width: 1200px; height: 1076px; overflow: hidden; background: var(--board); }
  .board { position: relative; width: 1200px; height: 1076px; background: var(--board); }

  .artist { font-family: "Marcellus", serif; color: var(--artist-red); line-height: 1; letter-spacing: 1px; font-weight: 400; }
  .song-title { font-family: "Marcellus", serif; color: var(--ink); line-height: 1.08; text-transform: uppercase; }

  /* Back cover */
  .back-cover { position: absolute; left: 26px; top: 34px; width: 610px; height: 496px; background: var(--paper); overflow: hidden; }
  .back-cover .spine { position: absolute; top: 0; width: 22px; height: 100%; background: var(--spine); }
  .back-cover .spine.left { left: 0; }
  .back-cover .spine.right { right: 0; }
  .spine-text { position: absolute; left: 11px; top: 200px; transform: translate(-50%, -50%) rotate(-90deg); white-space: nowrap;
    font-family: "Lora", serif; font-size: 7px; color: #ddd; letter-spacing: .3px; }
  .spine-text .red { color: var(--artist-red); }
  .back-art { position: absolute; left: 140px; top: 80px; width: 448px; height: 416px;
    background:
      linear-gradient(to right, var(--paper) 0%, rgba(255,255,255,0) 35%),
      linear-gradient(to bottom, var(--paper) 0%, var(--mountain-blue) 14%, var(--town-grey) 30%, #b8b6ae 42%, var(--bench-red) 50%, var(--bench-red) 62%, #d9dad6 72%, var(--snow) 100%);
    opacity: .9; }
  .back-cover .artist { position: absolute; left: 46px; top: 28px; font-size: 70px; }
  .back-cover .song-title { position: absolute; left: 50px; top: 113px; font-size: 33px; }
  .track-list { position: absolute; left: 62px; top: 214px; list-style: none; font-family: "Lora", serif; font-size: 16px; color: var(--ink); }
  .track-list li { height: 25.5px; }

  /* Front cover */
  .front-cover { position: absolute; left: 662px; top: 34px; width: 508px; height: 502px; background: var(--paper); overflow: hidden; }
  .front-art { position: absolute; inset: 0;
    background: linear-gradient(to bottom, var(--sky) 0%, var(--sky) 12%, var(--mountain-blue) 22%, var(--town-grey) 38%, #bdb8b0 48%, var(--bench-red) 55%, var(--bench-red) 70%, #d6d8d4 80%, var(--snow) 100%); }
  .front-cover .artist { position: absolute; left: 26px; top: 30px; font-size: 74px; }
  .front-cover .song-title { position: absolute; left: 26px; top: 118px; font-size: 38px; }

  /* CD */
  .cd { position: absolute; left: 370px; top: 549px; width: 500px; height: 500px; }
  .cd .artist-svg { font-family: "Marcellus", serif; fill: var(--artist-red); letter-spacing: 1px; }
  .cd .title-svg { font-family: "Marcellus", serif; fill: var(--ink); }

  .view-label { position: absolute; font-family: "Arimo", sans-serif; font-size: 26px; color: var(--label); }
</style>
</head>
<body>
<main class="board">

  <section class="back-cover">
    <div class="spine left"><span class="spine-text"><span class="red">MAVE</span> / PAPER BOATS AT DAWN</span></div>
    <div class="spine right"><span class="spine-text"><span class="red">MAVE</span> / PAPER BOATS AT DAWN</span></div>
    <div class="back-art" role="img" aria-label="Sketched illustration of an empty red bench on a snowy lookout above a town and mountains"></div>
    <h2 class="artist">MAVE</h2>
    <p class="song-title">Paper boats<br>at dawn</p>
    <ol class="track-list">
      <li>Song 1</li><li>Song 2</li><li>Song 3</li><li>Song 4</li><li>Song 5</li><li>Song 6</li><li>Song 7</li>
    </ol>
  </section>

  <section class="front-cover">
    <div class="front-art" role="img" aria-label="Sketched illustration of two friends seen from behind, hugging on a red bench overlooking a snowy town and mountains"></div>
    <h1 class="artist">MAVE</h1>
    <p class="song-title">Paper boats<br>at dawn</p>
  </section>

  <svg class="cd" viewBox="0 0 500 500" role="group" aria-label="CD disc label">
    <defs>
      <linearGradient id="cdArt" x1="0" y1="0" x2="0" y2="1">
        <stop offset="0" stop-color="#ffffff"/>
        <stop offset=".2" stop-color="#ffffff"/>
        <stop offset=".34" stop-color="#a9d3e6"/>
        <stop offset=".5" stop-color="#c9ccc8"/>
        <stop offset=".62" stop-color="#bdb8b0"/>
        <stop offset=".72" stop-color="#d8302e"/>
        <stop offset=".86" stop-color="#d8302e"/>
        <stop offset="1" stop-color="#e6e7e3"/>
      </linearGradient>
    </defs>
    <circle cx="250" cy="250" r="249" fill="url(#cdArt)" role="img" aria-label="Sketched illustration of two friends hugging on a red bench above a snowy town"/>
    <circle cx="250" cy="250" r="58" fill="none" stroke="#ffffff" stroke-width="2"/>
    <circle cx="250" cy="250" r="42" fill="#ffffff"/>
    <text class="artist-svg" x="58" y="168" font-size="62">MAVE</text>
    <text class="title-svg" x="244" y="129" font-size="28">PAPER BOATS</text>
    <text class="title-svg" x="244" y="166" font-size="28">AT DAWN</text>
  </svg>

  <span class="view-label" style="left:90px; top:545px;">Back Cover</span>
  <span class="view-label" style="left:864px; top:545px;">Front Cover</span>
  <span class="view-label" style="left:862px; top:950px;">CD Cover</span>

</main>
</body>
</html>
```